Bluewater Ridge Commercial Svcs

I need a business card for my company in Orlando Florida. I provide all property maintenance/repair services both commercial and residential. We also do kitchen and bath remodels, full gut rehab and renovation, and painting. I do not have any suggestions for card layout. I want something that looks great that i can hand out to contractors and home owners to help generate business.

Target Market(s)

contractors, property owners, real estate property managers

Industry/Entity Type

Business

Contact Information for Business Card

Bluewater Ridge Commercial Services, Dale Morrow, 2186 Tamsey Ln. Orlando,FL 32811, Owner

```html
<!DOCTYPE html>
<html lang="en">
<head>
<meta charset="utf-8">
<title>Bluewater Ridge Commercial Services – Business Card</title>
<link href="https://fonts.googleapis.com/css2?family=Open+Sans:wght@400;600;700&display=swap" rel="stylesheet">
<style>
  :root {
    --page-bg: #e4e4e2;
    --card-white: #ffffff;
    --panel-deep: #1f4f93;
    --panel-mid: #2a6bb0;
    --panel-light: #3a8ccb;
    --panel-edge: #1a2f5c;
    --divider: rgba(255,255,255,0.55);
    --text-light: #ffffff;
    --brand-blue: #2c64a8;
    --card-shadow: rgba(0,0,0,0.18);
  }
  * { box-sizing: border-box; margin: 0; padding: 0; }
  html, body {
    width: 1200px; height: 1129px; overflow: hidden;
    background: var(--page-bg);
    font-family: "Open Sans", Arial, sans-serif;
  }
  .canvas {
    position: relative; width: 1200px; height: 1129px;
    display: flex; justify-content: center; align-items: center; gap: 110px;
  }
  .card {
    position: relative; width: 420px; height: 735px;
    background: var(--card-white);
    box-shadow: 0 6px 22px var(--card-shadow);
    overflow: hidden;
  }
  /* front */
  .card-front { display: flex; flex-direction: column; align-items: center; }
  .brand-name {
    color: var(--brand-blue); font-weight: 600; font-size: 24px;
    text-align: center; line-height: 1.25; letter-spacing: 0.2px;
  }
  .card-front .brand-block { margin-top: 250px; display: flex; flex-direction: column; align-items: center; gap: 14px; }
  .brand-dot { width: 26px; height: 26px; border-radius: 50%; background: var(--brand-blue); }
  /* back */
  .top-band { height: 95px; background: var(--card-white); }
  .info-panel {
    height: 445px;
    border-top: 6px solid var(--panel-edge);
    background: radial-gradient(ellipse at 40% 85%, var(--panel-light) 0%, var(--panel-mid) 45%, var(--panel-deep) 100%);
    display: flex; flex-direction: column;
  }
  .info-row {
    display: flex; align-items: center; gap: 24px;
    padding: 0 26px; color: var(--text-light);
    border-bottom: 1px solid var(--divider);
  }
  .info-row:last-child { border-bottom: none; }
  .row-name { height: 99px; }
  .row-phone { height: 85px; }
  .row-email { height: 85px; }
  .row-address { flex: 1; align-items: flex-start; padding-top: 24px; }
  .icon-badge {
    flex: none; width: 46px; height: 46px; border-radius: 50%;
    background: var(--text-light); display: flex; align-items: center; justify-content: center;
  }
  .icon-badge svg { width: 24px; height: 24px; fill: var(--panel-mid); }
  .person-name { font-size: 26px; font-weight: 700; letter-spacing: 0.5px; line-height: 1.1; }
  .person-title { font-size: 18px; font-weight: 400; }
  .contact-text { font-size: 18px; font-weight: 400; }
  .address-text { font-size: 17px; line-height: 1.35; margin-top: 8px; }
  .bottom-band { height: 195px; display: flex; align-items: center; justify-content: center; }
  .bottom-band .brand-name { font-size: 21px; }
</style>
</head>
<body>
<main class="canvas">
  <section class="card card-front" aria-label="Card front">
    <div class="brand-block">
      <span class="brand-dot"></span>
      <p class="brand-name">Bluewater Ridge<br>Commercial Services</p>
    </div>
  </section>

  <section class="card card-back" aria-label="Card back">
    <div class="top-band"></div>
    <div class="info-panel">
      <div class="info-row row-name">
        <span class="icon-badge">
          <svg viewBox="0 0 24 24"><circle cx="12" cy="8" r="4.5"/><path d="M3.5 21c0-4.7 3.8-7.5 8.5-7.5s8.5 2.8 8.5 7.5z"/></svg>
        </span>
        <div>
          <p class="person-name">DALE MORROW</p>
          <p class="person-title">Marketing Director</p>
        </div>
      </div>
      <div class="info-row row-phone">
        <span class="icon-badge">
          <svg viewBox="0 0 24 24"><path d="M7 2h10a1.5 1.5 0 0 1 1.5 1.5v17A1.5 1.5 0 0 1 17 22H7a1.5 1.5 0 0 1-1.5-1.5v-17A1.5 1.5 0 0 1 7 2zm0.5 3v13h9V5zm4.5 14.2a1 1 0 1 0 0 2 1 1 0 0 0 0-2z"/></svg>
        </span>
        <p class="contact-text">(407) 555 0148</p>
      </div>
      <div class="info-row row-email">
        <span class="icon-badge">
          <svg viewBox="0 0 24 24"><path d="M2.5 5h19v14h-19zm1.8 1.6L12 12.6l7.7-6zM4 17.5h16V8.4l-8 6.2-8-6.2z"/></svg>
        </span>
        <p class="contact-text">dale@bluewaterridge.com</p>
      </div>
      <div class="info-row row-address">
        <span class="icon-badge">
          <svg viewBox="0 0 24 24"><path d="M12 2a7 7 0 0 0-7 7c0 5.2 7 13 7 13s7-7.8 7-13a7 7 0 0 0-7-7zm0 9.8a2.8 2.8 0 1 1 0-5.6 2.8 2.8 0 0 1 0 5.6z"/></svg>
        </span>
        <p class="address-text">2186 Tamsey Ln.<br>Orlando,FL 32811</p>
      </div>
    </div>
    <div class="bottom-band">
      <p class="brand-name">Bluewater Ridge<br>Commercial Services</p>
    </div>
  </section>
</main>
</body>
</html>
```